Quite like thee: needs a logo design and a business card

The business name is called: Quite like thee. It's all about fashion for everyone who needs to gain confidence and find his own style: Image Consultant, Personal Shopper. Here my Facebook fan page: https://www.facebook.com/pages/Quite-like-thee/318264907152839

I would like a smart logo & business card. The design has to be smart and long lasting. I like simplicity ("less is more"). The image needs to bring over seriousness and style. I target people from 35-65 years old. I would love to have smart warm colours like brown mole or anthracite, eventually with some berry or bordeaux red.

The copy is the following:
Quite like thee
Doreen Pavlik
Mobile: +27 72 463 08 29
eMail: pavlik.doreen@brightmailbox.net
Cape Town

Reason: I'm not in a rush.

Target Market(s)

Core target group: 35-65 years old women; wealthy; living in Cape Town
Larger target group: South Africa; eventually men too

Industry/Entity Type

Business

```html
<!DOCTYPE html>
<html lang="en">
<head>
<meta charset="utf-8">
<title>Quite like thee · Business card</title>
<link rel="stylesheet" href="https://fonts.googleapis.com/css2?family=Cormorant+Garamond:ital,wght@0,600;1,500&display=swap">
<style>
  :root {
    --backdrop: #4d1822;
    --mole: #7a5a4c;
    --mist: #c3d7e9;
    --mist-text: #cbd8ec;
    --gradient-mid: #a3989a;
    --name-brown: #7a5a4c;
  }
  html, body {
    margin: 0;
    padding: 0;
    width: 1200px;
    height: 1000px;
    overflow: hidden;
  }
  body {
    background: var(--backdrop);
    position: relative;
  }
  .card {
    position: absolute;
    top: 226px;
    width: 364px;
    height: 548px;
    box-sizing: border-box;
    display: flex;
    flex-direction: column;
    align-items: center;
    font-family: "Cormorant Garamond", Georgia, serif;
  }
  .card--front {
    left: 190px;
    background: var(--mole);
  }
  .card--back {
    left: 646px;
    background: linear-gradient(180deg, var(--mist) 0%, var(--gradient-mid) 42%, var(--mole) 62%, var(--mole) 100%);
  }
  .brand-name {
    margin: 0;
    font-weight: 600;
    font-style: normal;
    font-size: 38px;
    letter-spacing: 0.5px;
    line-height: 1;
  }
  .card--front .brand-name {
    margin-top: 122px;
    color: var(--mist-text);
  }
  .card--back .brand-name {
    margin-top: 118px;
    color: var(--name-brown);
  }
  .brand-dot {
    display: block;
    width: 96px;
    height: 96px;
    border-radius: 50%;
    background: var(--mist);
  }
  .card--front .brand-dot { margin-top: 56px; }
  .card--back .brand-dot { margin-top: 62px; }
  .contact {
    margin: 28px 0 0;
    padding: 0;
    list-style: none;
    text-align: center;
    font-style: italic;
    font-weight: 500;
    font-size: 23px;
    line-height: 37px;
    color: var(--mist-text);
  }
</style>
</head>
<body>
  <section class="card card--front" aria-label="Card front">
    <h1 class="brand-name">Quite like thee</h1>
    <span class="brand-dot" aria-hidden="true"></span>
  </section>

  <section class="card card--back" aria-label="Card back">
    <h2 class="brand-name">Quite like thee</h2>
    <span class="brand-dot" aria-hidden="true"></span>
    <ul class="contact">
      <li class="contact__name">Doreen Pavlik</li>
      <li class="contact__role">personalstylist</li>
      <li class="contact__phone">mobile: +27 72 463 08 29</li>
      <li class="contact__email">eMail: pavlik.doreen@brightmailbox.net</li>
      <li class="contact__city">cape town</li>
    </ul>
  </section>
</body>
</html>
```